The Lantern and the Meadow: A Quiet Bloom Within Us

We need a book cover/spine and back cover for a multi author book called the Lantern and The Meadow: A Quiet Bloom Within Us. This will be a collection of stories from women who major transformational stories to tell. They embark on a voyage, find themselves in uncharted territory, find friends or allies and in the end find themselves back home to themselves. I want this book cover to feel fun of wonder, adventure, intrigue with a a dainty energy. I have uploaded some images for inspiration but not to use in the design because they are not images I have permission to use.

```html
<!DOCTYPE html>
<html lang="en">
<head>
<meta charset="utf-8">
<title>The Lantern and the Meadow – Cover Wrap</title>
<link rel="stylesheet" href="https://fonts.googleapis.com/css2?family=Gilda+Display&family=Montserrat+Alternates:ital,wght@0,300;0,400;1,300&display=swap">
<style>
  :root {
    --paper: #ffffff;
    --olive-ink: #4a4a35;
    --olive-deep: #383d28;
    --ink: #1e1e1e;
    --soft-ink: #3a3a3a;
    --sky-top: #7ba7d9;
    --sky-low: #cdd6e2;
    --hill: #4d5a37;
    --field: #5e6b48;
    --field-low: #564e63;
    --white: #ffffff;
  }
  * { margin: 0; padding: 0; box-sizing: border-box; }
  html, body { width: 1200px; height: 849px; overflow: hidden; background: var(--paper); }
  .wrap { position: relative; width: 1200px; height: 849px; background: var(--paper); }

  .serif { font-family: "Gilda Display", Georgia, serif; }
  .sans { font-family: "Montserrat Alternates", "Helvetica Neue", sans-serif; }

  /* Back cover */
  .back-title {
    position: absolute; left: 0; width: 568px; top: 44px; text-align: center;
    font-size: 35px; color: var(--olive-ink); line-height: 1;
  }
  .back-subtitle {
    position: absolute; left: 0; width: 568px; top: 89px; text-align: center;
    font-size: 20px; font-weight: 300; color: var(--olive-ink); letter-spacing: 0.5px;
  }
  .blurb-heading {
    position: absolute; left: 104px; top: 159px;
    font-size: 18px; font-weight: 400; color: var(--ink);
  }
  .blurb {
    position: absolute; left: 67px; top: 198px; width: 290px;
    font-size: 15.5px; line-height: 20.5px; font-weight: 300; color: var(--ink);
  }
  .pill {
    position: absolute; left: 390px; top: 172px; width: 111px; height: 186px;
    border-radius: 56px; background: var(--olive-deep);
  }
  .quote {
    position: absolute; left: 80px; width: 432px; top: 482px; text-align: center;
    font-size: 20px; line-height: 26.3px; font-style: italic; font-weight: 300; color: var(--soft-ink);
  }

  /* Spine */
  .spine {
    position: absolute; left: 585px; top: 161px; height: 650px; width: 32px;
    writing-mode: vertical-rl; transform: rotate(180deg);
    white-space: nowrap; font-size: 25px; color: var(--soft-ink);
    display: flex; align-items: center; justify-content: center;
  }
  .spine .sans { font-weight: 300; }

  /* Front cover */
  .front-photo {
    position: absolute; left: 633px; top: 0; width: 567px; height: 849px;
    background: linear-gradient(180deg, var(--sky-top) 0%, #a9bfdc 22%, var(--sky-low) 45%, var(--hill) 52%, var(--field) 64%, #4f5a40 80%, var(--field-low) 100%);
  }
  .front-subtitle {
    position: absolute; left: 633px; width: 567px; top: 50px; text-align: center;
    font-size: 36px; font-weight: 300; color: var(--white); white-space: nowrap;
  }
  .front-title {
    position: absolute; left: 633px; width: 567px; top: 570px; text-align: center;
    color: var(--white); line-height: 1;
  }
  .front-title .big { display: block; font-size: 70px; }
  .front-title .small { display: block; font-size: 42px; margin: -2px 0 -4px; }
</style>
</head>
<body>
<main class="wrap">
  <section class="back-cover">
    <h2 class="back-title serif">The Lantern and the Meadow</h2>
    <p class="back-subtitle sans">A Quiet Bloom Within Us</p>
    <h3 class="blurb-heading sans">Laoreet Dolore Magna</h3>
    <p class="blurb sans">Lorem ipsum dolor sit amet,<br>consectetuer adipiscing elit, sed<br>diam nonummy nibh euismod<br>tincidunt ut laoreet dolore magna<br>aliquam erat volutpat. Ut wisi<br>enim ad minim veniam, quis<br>nostrud exerci tation ullamcorper<br>suscipit lobortis nisl ut aliquip ex</p>
    <div class="pill" aria-hidden="true"></div>
    <p class="quote sans">Lorem ipsum dolor sit amet consec-<br>tetuer adipiscing elit sed diam nonum-<br>my nibh euismod tincidunt ut laoreet<br>dolore magna aliquam erat volutpa</p>
  </section>

  <div class="spine"><span class="serif">The Lantern and the Meadow:&nbsp;</span><span class="sans">A Quiet Bloom Within Us</span></div>

  <section class="front-cover">
    <div class="front-photo" role="img" aria-label="Photograph of a woman with long fair hair, seen from behind, walking through a meadow of purple wildflowers under a clear blue sky, holding a bunch of flowers"></div>
    <p class="front-subtitle sans">A Quiet Bloom Within Us</p>
    <h1 class="front-title serif">
      <span class="big">The Lantern</span>
      <span class="small">and</span>
      <span class="big">the Meadow:</span>
    </h1>
  </section>
</main>
</body>
</html>
```